Flyer Design

I'm looking for a new flyer design to help promote our landscape company, and some of our main service for the up and coming season. We're trying to position ourselves as a leader in our market, so obviously quality is important to us.

Our current promotion is 25% off the first month with signup of annual service.

Phone Number: (816) 555-0193
Website: gardelvista.com
Our tagline: "Your hands are full... Let us help"

The call to action: direct them to our website for a detailed list of services and to receive a free quote.

You're welcome to add your own wording and punctuation. If I like the design I will provide feedback accordingly.

I have attached a jpg of our logo to help with design colors. I will provide the vector file upon completion of this project.

Also, I've attached a few photos that I had on hand of our companies work that may help with the design. Obviously I don't want to use them all, but there are a couple just to help out. I'm not opposed to stock photos either.
Thanks

Target Market(s)

We market to high end customers, generally with home between $500k-$2mil, or household income over $200k. Quality and creativity are most important to us.

Industry/Entity Type

Landscape

Requirements
Must have
• Creativity, easy to read, modern style.

```html
<!DOCTYPE html>
<html lang="en">
<head>
<meta charset="utf-8">
<title>Gardel Vista – Spring Service Flyer</title>
<link rel="stylesheet" href="https://fonts.googleapis.com/css2?family=Montserrat:wght@700;900&family=Didact+Gothic&display=swap">
<style>
  :root {
    --page-bg: #e7e4df;
    --paper: #f1f1f1;
    --paper-shade: #dcdcdc;
    --ink: #2a2a2a;
    --ink-soft: #555555;
    --orange: #e0651b;
    --olive: #4b5039;
    --white: #ffffff;
    --lawn: #5f9a3a;
    --lawn-light: #a9c98a;
    --house: #b9a48a;
  }
  html, body {
    margin: 0;
    width: 1200px;
    height: 1000px;
    overflow: hidden;
    background: var(--page-bg);
  }
  .flyer {
    position: absolute;
    left: 250px;
    top: 30px;
    width: 700px;
    height: 940px;
    box-shadow: 0 10px 30px rgba(0,0,0,0.18);
  }
  .flyer svg { display: block; }
  .headline { font-family: "Montserrat", sans-serif; font-weight: 900; }
  .label { font-family: "Montserrat", sans-serif; font-weight: 700; }
  .body-copy { font-family: "Didact Gothic", sans-serif; }
</style>
</head>
<body>
<div class="flyer">
  <svg width="700" height="940" viewBox="0 0 700 940" xmlns="http://www.w3.org/2000/svg">
    <defs>
      <linearGradient id="paper-grad" x1="0" y1="0" x2="1" y2="1">
        <stop offset="0" stop-color="var(--paper-shade)"/>
        <stop offset="0.45" stop-color="var(--paper)"/>
        <stop offset="1" stop-color="var(--paper-shade)"/>
      </linearGradient>
      <linearGradient id="lawn-top" x1="0" y1="0" x2="0" y2="1">
        <stop offset="0" stop-color="var(--house)"/>
        <stop offset="0.5" stop-color="#7d8a5c"/>
        <stop offset="1" stop-color="var(--lawn)"/>
      </linearGradient>
      <linearGradient id="lawn-bottom" x1="0" y1="0" x2="0" y2="1">
        <stop offset="0" stop-color="#cfe0ee"/>
        <stop offset="0.35" stop-color="var(--house)"/>
        <stop offset="0.7" stop-color="var(--lawn)"/>
        <stop offset="1" stop-color="var(--lawn-light)"/>
      </linearGradient>
    </defs>

    <!-- paper -->
    <rect class="paper" width="700" height="940" fill="url(#paper-grad)"/>

    <!-- top project photo -->
    <polygon class="photo-top" role="img" aria-label="Photo of a stucco home with a freshly striped front lawn"
             points="240,0 700,0 700,200 240,90" fill="url(#lawn-top)" stroke="var(--white)" stroke-width="8"/>
    <polygon class="photo-chevron" points="292,98 268,112 292,126 284,112" fill="var(--orange)"/>

    <!-- website preview -->
    <rect class="laptop-preview" role="img" aria-label="Laptop showing the company website"
          x="30" y="40" width="210" height="150" rx="10" fill="#b9bcbf"/>

    <!-- diagonal offer block -->
    <g class="offer" transform="rotate(-16 350 430)">
      <text class="label" x="60" y="262" font-size="19" fill="var(--orange)">SIGN UP NOW! WWW.GARDELVISTA.COM</text>
      <line x1="60" y1="274" x2="560" y2="274" stroke="var(--ink-soft)" stroke-width="1.5"/>
      <polyline points="62,288 74,298 62,308" fill="none" stroke="var(--ink)" stroke-width="3"/>
      <text class="body-copy" x="84" y="305" font-size="18" fill="var(--ink-soft)">SNOW REMOVAL | MOWING | TREE MAINTENANCE | AERATION</text>

      <text class="headline" x="200" y="390" font-size="88" fill="var(--ink)">EARN</text>
      <text class="headline" x="160" y="478" font-size="88" fill="var(--orange)">25% OFF</text>
      <text class="headline" x="330" y="556" font-size="76" fill="var(--ink)">TODAY</text>
      <line x1="200" y1="580" x2="640" y2="580" stroke="var(--ink-soft)" stroke-width="1.5"/>

      <text class="body-copy" text-anchor="end" font-size="20" fill="var(--ink-soft)">
        <tspan x="620" y="614">Visit our site and sign up to receive</tspan>
        <tspan x="620" y="642">25% off your first month</tspan>
        <tspan x="620" y="670">of annual service.</tspan>
      </text>
    </g>

    <!-- company name -->
    <g class="brand">
      <circle cx="488" cy="690" r="13" fill="var(--orange)"/>
      <text class="label" x="510" y="699" font-size="26" fill="var(--ink)">Gardel Vista</text>
    </g>

    <!-- bottom project photo -->
    <polygon class="photo-bottom" role="img" aria-label="Photo of a two-storey home with manicured lawn and shrubs"
             points="0,640 420,700 420,940 0,940" fill="url(#lawn-bottom)" stroke="var(--white)" stroke-width="8"/>

    <!-- tagline -->
    <text class="body-copy" x="404" y="790" font-size="17" fill="var(--ink)" transform="rotate(-14 404 790)">“Your hands are full... Let us help”</text>

    <!-- contact band -->
    <polygon class="contact-band" points="420,830 700,760 700,940 420,940" fill="var(--olive)"/>
    <g class="phone-icon">
      <circle cx="462" cy="884" r="26" fill="var(--orange)" stroke="var(--white)" stroke-width="3"/>
      <path d="M452 872 q-4 4 2 14 q7 10 14 10 l4 -4 l-6 -5 l-3 3 q-5 -3 -8 -9 l3 -3 z" fill="var(--white)"/>
    </g>
    <text class="label" x="500" y="884" font-size="27" fill="var(--white)">816.555.0193</text>
    <text class="label" x="502" y="910" font-size="15" fill="var(--white)">www.gardelvista.com</text>
  </svg>
</div>
</body>
</html>
```